Red Kettle Handcrafted Tomato Ketchup packaging design modern

From the best ingredients there is the best ketchup Red Handcrafted ketchup are specially formulated for fine dining and drinks, bringing out all the flavors. As the Red Kettle handcrafted ketchup is otherwise fabulous: Made with wholesome, fully ripe fruits Nothing with half things! All Red Kettle handcrafted ketchups are pure nature, without any artificial diluents or concentrates. Where tomato is on it, that's all there is to it - guaranteed! the design should be professional and noble despite being trendy. A watcher wants to sell the ketchup as merchandising from our restaurant. but as a single brand positioning. The ketchup is vegan. Dimensions: 6.8 cm Height: 7.8 cm Circumference: 21.6 cm The text down (Text 1-4). The lid of the text the glass packaging is black! Thanks for your efforts. I look forward to your designs.

Target Market(s)

foodies

Font styles to use
Serif
Sans Serif

Colors

Designer to choose colors to be used in the design.

Requirements
Must have
• Title: (Handcrafted Tomato Ketchup) Text One: (Store chilled after opening and consume quickly, pasteurized.) Text Two: (Handcrafted in Switzerland by Brentwick Gastro GmbH, Chur www.redkettle-example.ch) Text Tree: (Tomatoes, White Wine Vinegar, Aceto Balsamico, Brown Cane Sugar, Corn Starch, Spices, Salt) Text For: (200 grams) or (200g) The Logo of Red Kettle with the Pasta and Wine have to because of the gesety.
Nice to have
• small vegan icon (maybe)
Should not have
• text of the logo (pasta & wine)

```html
<!DOCTYPE html>
<html lang="en">
<head>
<meta charset="utf-8">
<title>Red Kettle – Handcrafted Tomato Ketchup Label</title>
<link rel="stylesheet" href="https://fonts.googleapis.com/css2?family=Federo&family=Oswald:wght@600&display=swap">
<style>
  :root {
    --backdrop: #eceef1;
    --label-white: #f4f4f2;
    --mustard: #e2c723;
    --ink: #23222a;
  }
  * { margin: 0; padding: 0; box-sizing: border-box; }
  html, body { width: 1200px; height: 1200px; overflow: hidden; }
  body { background: var(--backdrop); position: relative; font-family: "Federo", sans-serif; color: var(--ink); }

  .label {
    position: absolute; left: 204px; top: 135px;
    width: 792px; height: 930px;
    background: var(--label-white);
    box-shadow: 0 6px 24px rgba(0,0,0,0.08);
  }
  .label-shape { position: absolute; inset: 0; }
  .label-content { position: absolute; inset: 0; text-align: center; }

  .brand-name {
    position: absolute; left: 0; right: 0; top: 160px;
    font-family: "Federo", sans-serif; font-size: 104px; line-height: 1;
    letter-spacing: 2px;
  }
  .product-title {
    position: absolute; left: 0; right: 0; top: 295px;
    display: flex; justify-content: center; align-items: center; gap: 14px;
  }
  .product-title .dash { width: 46px; height: 2px; background: var(--ink); }
  .product-title h2 {
    font-family: "Oswald", sans-serif; font-weight: 600; font-style: italic;
    font-size: 36px; line-height: 1; letter-spacing: 0.5px;
    padding: 10px 8px 12px;
    border-top: 2px solid var(--ink); border-bottom: 2px solid var(--ink);
  }
  .storage-note {
    position: absolute; left: 0; right: 0; top: 490px;
    font-size: 26px; line-height: 36px;
  }
  .maker-info {
    position: absolute; left: 0; right: 0; top: 588px;
    font-size: 18px; line-height: 25px;
  }
  .ingredients {
    position: absolute; left: 0; right: 0; top: 692px;
    font-size: 18px; line-height: 26px;
  }
  .net-weight {
    position: absolute; left: 0; right: 0; top: 832px;
    font-size: 18px;
  }
</style>
</head>
<body>
  <section class="label">
    <svg class="label-shape" width="792" height="930" viewBox="0 0 792 930" aria-hidden="true">
      <polygon points="120,0 672,0 792,170 792,760 672,930 120,930 0,760 0,170" fill="var(--mustard)"/>
    </svg>
    <div class="label-content">
      <h1 class="brand-name">RED KETTLE</h1>
      <div class="product-title">
        <span class="dash"></span>
        <h2>HANDCRAFTED TOMATO KETCHUP</h2>
        <span class="dash"></span>
      </div>
      <p class="storage-note">Store chilled<br>after opening and consume quickly, pasteurized.</p>
      <p class="maker-info">Handcrafted in Switzerland<br>by Brentwick Gastro GmbH, Chur<br>www.redkettle-example.ch</p>
      <p class="ingredients">Tomatoes, White Wine Vinegar, Aceto Balsamico,<br>Brown Cane Sugar, Corn Starch, Spices, Salt</p>
      <p class="net-weight">200 grams</p>
    </div>
  </section>
</body>
</html>
```